Lip Balm Label Design

Design a label for a Lavender-Mint lip balm. We make high-quality natural essential oil products. Please use the old label as an example of what exists. The label should include purple. The final design should be eye-catching and distinct. The file should be in an AI file.

Here is the information that should be included on the label:
1) ingredients:Theobroma Cacao (Cocoa) Seed Butter, Theobroma grandiflorum Ultra Refined Butter, beesewax, Calendula Officinalis Flower Oil, Prunus Amygdalus Dulcis (Sweet Almond) Oil, cetyl alcohol and Tocopherol. Lavandula Angustifolia (Lavender) Oil and Mentha Piperita (Peppermint) Oil.

2) www.kelvorascent.com

3) Brand name and logo: K. Velora Aromatherapy (logo is attached- you can use with form)

```html
<!DOCTYPE html>
<html lang="en">
<head>
<meta charset="UTF-8">
<title>Lavender Mint Lip Balm Label</title>
<link href="https://fonts.googleapis.com/css2?family=Cormorant+Garamond:wght@400;500&family=Allura&family=Josefin+Sans:wght@300;400&display=swap" rel="stylesheet">
<style>
  :root {
    --backdrop: #4f3f73;
    --label-white: #fbfbfe;
    --band-lilac: #b9b3d8;
    --plum: #5e4f86;
    --lilac-soft: #a39bc9;
    --mint-script: #b3abd4;
    --leaf-green: #6aa33a;
    --sprig-light: #c9bfe6;
    --sprig-deep: #8d7cc0;
    --ingredient-text: #ffffff;
  }
  * { margin: 0; padding: 0; box-sizing: border-box; }
  html, body {
    width: 1200px; height: 1200px; overflow: hidden;
    background: var(--backdrop);
  }
  .label {
    position: absolute; left: 220px; top: 117px;
    width: 760px; height: 966px;
    background: var(--label-white);
    overflow: hidden;
  }
  .ingredient-band {
    position: absolute; left: 556px; top: 0;
    width: 204px; height: 100%;
    background: var(--band-lilac);
  }
  .soft-drop {
    position: absolute; left: 40px; top: 180px;
    width: 300px; height: 620px;
  }
  .brand {
    position: absolute; left: 106px; top: 58px;
    display: flex; align-items: center; gap: 12px;
  }
  .brand-dot {
    width: 34px; height: 34px; border-radius: 50%;
    background: var(--leaf-green);
  }
  .brand-name {
    font-family: "Cormorant Garamond", serif;
    font-weight: 500; font-size: 30px;
    color: var(--leaf-green);
    letter-spacing: 0.02em;
  }
  .rotate-up {
    position: absolute;
    transform-origin: 0 0;
    transform: rotate(-90deg);
    white-space: nowrap;
  }
  .rotate-down {
    position: absolute;
    transform-origin: 0 0;
    transform: rotate(90deg);
    white-space: nowrap;
  }
  .product-name {
    left: 100px; top: 740px;
    font-family: "Cormorant Garamond", serif;
    font-weight: 400; font-size: 98px; line-height: 1;
    letter-spacing: 0.05em;
    color: var(--plum);
  }
  .flavour-script {
    left: 196px; top: 722px;
    font-family: "Allura", cursive;
    font-size: 160px; line-height: 1;
    color: var(--mint-script);
  }
  .product-type {
    position: absolute; left: 104px; top: 790px;
    font-family: "Josefin Sans", sans-serif;
    font-weight: 300; font-size: 48px;
    letter-spacing: 0.16em;
    color: var(--lilac-soft);
  }
  .net-weight {
    position: absolute; left: 105px; top: 864px;
    font-family: "Josefin Sans", sans-serif;
    font-weight: 300; font-size: 24px;
    color: var(--plum);
  }
  .web-address {
    left: 500px; top: 712px;
    font-family: "Josefin Sans", sans-serif;
    font-size: 10px; letter-spacing: 0.2em;
    color: var(--plum);
  }
  .sprig-art {
    position: absolute; left: 372px; top: 158px;
    width: 176px; height: 520px;
    border-radius: 88px 88px 30px 30px;
    background: linear-gradient(160deg, var(--sprig-light) 0%, var(--sprig-deep) 60%, rgba(141,124,192,0.35) 100%);
    opacity: 0.85;
  }
  .ingredients {
    left: 652px; top: 878px;
    width: 795px;
    white-space: normal;
    font-family: "Josefin Sans", sans-serif;
    font-weight: 400; font-size: 14px; line-height: 1.6;
    text-align: justify;
    text-transform: uppercase;
    color: var(--ingredient-text);
  }
</style>
</head>
<body>
  <div class="label">
    <div class="ingredient-band"></div>

    <svg class="soft-drop" viewBox="0 0 300 620" aria-hidden="true">
      <path d="M240 0 C 120 160, 0 360, 40 520 C 70 620, 260 640, 290 470 C 320 300, 250 140, 240 0 Z" fill="#eeecf7" opacity="0.7"/>
    </svg>

    <div class="brand">
      <span class="brand-dot"></span>
      <span class="brand-name">K. Velora Aromatherapy</span>
    </div>

    <div class="sprig-art" role="img" aria-label="Illustration of a lavender sprig with purple blossoms"></div>

    <div class="rotate-up product-name">LAVENDER</div>
    <div class="rotate-up flavour-script">mint</div>

    <div class="product-type">LIP BALM</div>
    <div class="net-weight">0.15 OZ (4.4 ML)</div>

    <div class="rotate-down web-address">www.kelvorascent.com</div>

    <p class="rotate-up ingredients">Ingredients: Theobroma Cacao (Cocoa) Seed Butter, Theobroma Grandiflorum Ultra Refined Butter, Beesewax, Calendula Officinalis Flower Oil, Prunus Amygdalus Dulcis (Sweet Almond) Oil, Cetyl Alcohol and Tocopherol. Lavandula Angustifolia (Lavender) Oil and Mentha Piperita (Peppermint) Oil.</p>
  </div>
</body>
</html>
```